Business card design needed

We need a buisness card design to suit our buisness "Bright Parcels", a company on the south coast of Australia, a wholesale greeting card and gift wrap buisness. We are open to different colour options possibly some pastels. A card that got my attention was'the ''trackbeacon.com.au'' buisness card. I liked the colour scheme, layout, and the use of a cartoon image, but am also open to all ideas.

Industry/Entity Type

Business

Contact Information for Business Card

Bright Parcels Unit 31 / 17 Morwell ave Southbrook 2562 ph 0247835108 fax 0247835109 Colin Maskey email bright.parcels@mailverra.com

```html
<!DOCTYPE html>
<html lang="en">
<head>
<meta charset="utf-8">
<title>Bright Parcels — Business Card</title>
<link rel="stylesheet" href="https://fonts.googleapis.com/css2?family=Lato:wght@300;400&display=swap">
<style>
  :root {
    --backdrop: #d6d6d6;
    --red-deep: #a5161c;
    --red-mid: #c0272d;
    --red-soft: #d0545a;
    --charcoal-deep: #1f2022;
    --charcoal-soft: #5c5d60;
    --accent-red: #c8262c;
    --text-light: #f2f2f2;
  }
  * { box-sizing: border-box; margin: 0; padding: 0; }
  html, body {
    width: 1200px; height: 900px; overflow: hidden;
    background: var(--backdrop);
    font-family: "Lato", sans-serif;
  }
  .canvas { position: relative; width: 1200px; height: 900px; }
  .card {
    position: absolute; left: 285px; width: 630px; height: 360px;
    overflow: hidden;
    box-shadow: 0 6px 18px rgba(0,0,0,0.18);
  }
  .card-front {
    top: 60px;
    background: linear-gradient(160deg, var(--red-deep) 0%, var(--red-mid) 55%, var(--red-soft) 100%);
  }
  .card-back {
    top: 480px;
    background: linear-gradient(160deg, var(--charcoal-deep) 0%, #333437 50%, var(--charcoal-soft) 100%);
  }

  /* front */
  .gift-art { position: absolute; top: 0; right: 30px; width: 300px; height: 160px; }
  .corner-bow { position: absolute; top: 0; left: 0; width: 90px; height: 80px; }
  .front-name {
    position: absolute; left: 36px; top: 232px;
    font-weight: 300; font-size: 38px; letter-spacing: 1px;
    color: var(--text-light); white-space: nowrap;
  }

  /* back */
  .back-brand {
    position: absolute; left: 0; top: 250px;
    display: flex; align-items: center; gap: 22px;
  }
  .brand-square { width: 42px; height: 26px; background: var(--accent-red); }
  .back-name {
    font-weight: 300; font-size: 36px; letter-spacing: 1px;
    color: var(--text-light); white-space: nowrap;
  }
  .contact-block {
    position: absolute; right: 22px; bottom: 26px;
    display: flex; gap: 8px;
    font-size: 11px; line-height: 1.45; font-weight: 400;
    color: var(--text-light); white-space: nowrap;
  }
  .contact-address { font-style: normal; }
  .contact-divider { width: 1px; background: var(--accent-red); }
</style>
</head>
<body>
<main class="canvas">

  <section class="card card-front" aria-label="Business card front">
    <svg class="corner-bow" viewBox="0 0 90 80" role="img" aria-label="Red satin ribbon bow tied across the top-left corner">
      <defs>
        <linearGradient id="bowTone" x1="0" y1="0" x2="1" y2="1">
          <stop offset="0" stop-color="#e0242b"/>
          <stop offset="1" stop-color="#9b1116"/>
        </linearGradient>
      </defs>
      <polygon points="0,0 90,0 0,80" fill="url(#bowTone)"/>
    </svg>
    <svg class="gift-art" viewBox="0 0 300 160" role="img" aria-label="White line-drawn gift bow beside a gift box filled with a floral folk pattern">
      <defs>
        <linearGradient id="giftTone" x1="0" y1="0" x2="1" y2="1">
          <stop offset="0" stop-color="#e9b9bb"/>
          <stop offset="1" stop-color="#c8474d"/>
        </linearGradient>
      </defs>
      <rect x="0" y="0" width="300" height="160" fill="url(#giftTone)" opacity="0.55"/>
    </svg>
    <p class="front-name">Bright Parcels</p>
  </section>

  <section class="card card-back" aria-label="Business card back">
    <div class="back-brand">
      <span class="brand-square"></span>
      <p class="back-name">Bright Parcels</p>
    </div>
    <div class="contact-block">
      <address class="contact-address">
        Unit 31 / 17<br>Morwell ave<br>Southbrook<br>2562
      </address>
      <span class="contact-divider"></span>
      <p class="contact-lines">
        Ph: 0247835108<br>Fax: 0247835109<br>bright.parcels@mailverra.com
      </p>
    </div>
  </section>

</main>
</body>
</html>
```